Quiet Harbor Hours Podcast Artwork

I need a cover for my podcast Quiet Harbor Hours that is clean, modern, and minimalist, but not too feminine

Target Market(s)

People struggling with fertility particularly women who are between the ages of 35-45 though there is a small set of listeners who are men

Requirements
Must have
• Embryo in the Zero
Should not have
• No script text

```html
<!DOCTYPE html>
<html lang="en">
<head>
<meta charset="utf-8">
<title>Quiet Harbor Hours Podcast Cover</title>
<link rel="stylesheet" href="https://fonts.googleapis.com/css2?family=League+Spartan:wght@700&family=Montserrat:wght@400&display=swap">
<style>
  :root {
    --stage: #eef0ee;
    --cover-white: #ffffff;
    --peach: rgba(246, 196, 172, 0.55);
    --peach-soft: rgba(249, 214, 196, 0.45);
    --sage: #9fb08b;
    --sage-light: #c5d0b8;
    --tan: #c8b48e;
    --embryo: #cfb88f;
    --brown: #7d5640;
    --ink: #2d2d2d;
  }
  * { margin: 0; padding: 0; box-sizing: border-box; }
  html, body {
    width: 1200px;
    height: 675px;
    overflow: hidden;
    background: var(--stage);
  }
  .stage {
    width: 1200px;
    height: 675px;
    display: flex;
    align-items: center;
    justify-content: center;
  }
  .cover {
    position: relative;
    width: 600px;
    height: 600px;
    background:
      radial-gradient(ellipse 260px 220px at 8% 10%, var(--peach-soft), transparent 70%),
      radial-gradient(ellipse 300px 260px at 96% 92%, var(--peach), transparent 70%),
      radial-gradient(ellipse 200px 180px at 90% 55%, var(--peach-soft), transparent 70%),
      var(--cover-white);
    box-shadow: 0 8px 24px rgba(0, 0, 0, 0.12);
    overflow: hidden;
  }
  .cover-mark {
    position: absolute;
    left: 190px;
    top: 70px;
    width: 230px;
    height: 230px;
    border-radius: 50%;
    background: radial-gradient(circle at 50% 50%, var(--embryo) 0%, #e6dcc6 38%, var(--sage-light) 40%, var(--sage) 100%);
  }
  .title-row {
    position: absolute;
    left: 76px;
    right: 76px;
    top: 352px;
    display: flex;
    align-items: center;
    gap: 14px;
  }
  .title-row::before,
  .title-row::after {
    content: "";
    flex: 1;
    height: 2px;
    background: var(--tan);
  }
  .title-top {
    font-family: "League Spartan", sans-serif;
    font-weight: 700;
    font-size: 44px;
    line-height: 1;
    color: var(--tan);
    white-space: nowrap;
  }
  .title-main {
    position: absolute;
    left: 0;
    right: 0;
    top: 412px;
    text-align: center;
    font-family: "League Spartan", sans-serif;
    font-weight: 700;
    font-size: 100px;
    line-height: 1;
    letter-spacing: 1px;
    color: var(--brown);
  }
  .podcast-label {
    position: absolute;
    left: 0;
    right: 0;
    top: 514px;
    display: flex;
    justify-content: center;
    align-items: center;
    gap: 8px;
    font-family: "Montserrat", sans-serif;
    font-weight: 400;
    font-size: 19px;
    letter-spacing: 10px;
    color: var(--ink);
  }
  .mic-icon { width: 12px; height: 22px; }
</style>
</head>
<body>
  <main class="stage">
    <section class="cover">
      <div class="cover-mark" role="img" aria-label="Sage ring with an embryo illustration in its centre"></div>
      <h1>
        <span class="title-row"><span class="title-top">QUIET HARBOR</span></span>
        <span class="title-main">HOURS</span>
      </h1>
      <p class="podcast-label">
        <svg class="mic-icon" viewBox="0 0 12 22" aria-hidden="true">
          <rect x="2.5" y="0" width="7" height="13" rx="3.5" fill="var(--ink)"/>
          <path d="M1 9 v2 a5 5 0 0 0 10 0 v-2" fill="none" stroke="var(--ink)" stroke-width="1.4"/>
          <rect x="5.3" y="16" width="1.4" height="4" fill="var(--ink)"/>
          <rect x="2" y="20" width="8" height="1.6" fill="var(--ink)"/>
        </svg>
        <span>PODCAST</span>
      </p>
    </section>
  </main>
</body>
</html>
```